Flyer für ein Onlineportal für private Vermieter
Design hat direkt unseren Geschmack getroffen.
Zielgruppe
Onlineportal für private Vermieter. Zentrale Botschaft: Mieterhöhungen sind in Orten ohne Mietspiegel fast unmöglich. Die Lösung? Ortsübliche Vergleichsmieten. Unsere Plattform bietet Zugang zu ortsüblichen Vergleichsmieten.
Aufgabenstellung
Stock-Bilder bitte von Velmora Bildarchiv, weil wir hier ein Abonnement haben.

```html
<!DOCTYPE html>
<html lang="de">
<head>
<meta charset="utf-8">
<title>Hallwerk – Nachhaltig vermieten</title>
<link href="https://fonts.googleapis.com/css2?family=Montserrat:wght@400;500;700;800&display=swap" rel="stylesheet">
<style>
  :root {
    --blue: #1fa9e1;
    --black: #151515;
    --white: #ffffff;
    --stage: #a9aeae;
    --ink: #1a1a1a;
  }
  * { margin: 0; padding: 0; box-sizing: border-box; }
  html, body { width: 1200px; height: 2352px; overflow: hidden; background: var(--stage); }
  body { font-family: "Montserrat", Arial, sans-serif; position: relative; }

  .flyer {
    position: absolute; left: 60px; top: 414px;
    width: 871px; height: 1229px;
    background: var(--white);
    transform: scale(1.24); transform-origin: 0 0;
    overflow: hidden;
  }
  .shapes { position: absolute; inset: 0; width: 871px; height: 1229px; }

  .title-band {
    position: absolute; left: 410px; top: 32px; width: 440px;
    text-align: center; color: var(--white);
    font-weight: 800; font-size: 30px; letter-spacing: 0.5px;
  }

  .brand {
    position: absolute; left: 70px; top: 78px;
    display: flex; align-items: center; gap: 14px;
    color: var(--black); font-weight: 700; font-size: 40px;
  }
  .brand-mark { width: 34px; height: 34px; background: var(--blue); }

  .hero-photo { position: absolute; inset: 0; }

  .intro { position: absolute; left: 51px; top: 212px; width: 345px; color: var(--white); }
  .intro h1 { font-weight: 800; font-size: 31px; line-height: 35px; margin-bottom: 12px; }
  .intro p { font-size: 15.6px; line-height: 21.6px; }

  .state-box { position: absolute; left: 91px; top: 565px; width: 312px; color: var(--white); }
  .state-box h2 { font-weight: 700; font-size: 21px; line-height: 25px; margin-bottom: 10px; }
  .state-box p { font-size: 15.4px; line-height: 20.6px; margin-bottom: 13px; }

  .rent-why { position: absolute; left: 477px; top: 595px; width: 352px; color: var(--ink); }
  .rent-why h2 { color: var(--blue); font-weight: 700; font-size: 21px; line-height: 25px; margin-bottom: 12px; }
  .rent-why p { font-size: 15.4px; line-height: 20.6px; margin-bottom: 12px; }

  .solution { position: absolute; left: 51px; top: 955px; width: 385px; color: var(--ink); }
  .solution h2 { color: var(--blue); font-weight: 700; font-size: 21px; line-height: 25.5px; margin-bottom: 10px; }
  .solution p { font-size: 15.4px; line-height: 20.6px; }

  .web {
    position: absolute; left: 51px; top: 1172px;
    color: var(--white); font-weight: 700; font-size: 19px; letter-spacing: 2.5px;
    white-space: nowrap;
  }
</style>
</head>
<body>
  <main class="flyer">
    <svg class="shapes" viewBox="0 0 871 1229" aria-hidden="true">
      <polygon points="285,0 871,0 871,140 372,140" fill="var(--blue)"/>
      <polygon points="322,0 871,0 871,124 398,124" fill="var(--white)"/>
      <polygon points="340,0 871,0 871,112 408,112" fill="var(--black)"/>
      <polygon points="0,183 871,183 871,572 0,572" fill="var(--blue)"/>
      <polygon points="380,205 400,183 430,183 445,208" fill="var(--black)"/>
      <rect x="0" y="572" width="871" height="560" fill="var(--white)"/>
      <polygon points="45,520 405,520 435,550 435,925 75,925 50,900 50,572 10,572" fill="var(--black)"/>
      <polygon points="0,1117 370,1117 400,1135 0,1135" fill="var(--black)"/>
      <polygon points="0,1140 355,1140 400,1229 0,1229" fill="var(--blue)"/>
      <polygon points="372,1117 420,1117 455,1200 871,1200 871,1212 440,1212" fill="var(--black)"/>
      <polygon points="360,1140 380,1140 420,1229 400,1229" fill="var(--white)"/>
      <rect x="440" y="1218" width="431" height="11" fill="var(--blue)"/>
    </svg>

    <div class="title-band">NACHHALTIG VERMIETEN</div>

    <div class="brand"><span class="brand-mark"></span>Hallwerk</div>

    <svg class="hero-photo" viewBox="0 0 871 1229" role="img"
         aria-label="Stockfoto von Velmora Bildarchiv: Beraterin und Vermieter im Gespräch am Tisch mit Hausmodell">
      <defs>
        <linearGradient id="photoTone" x1="0" y1="0" x2="1" y2="1">
          <stop offset="0" stop-color="#e7e4df"/>
          <stop offset="0.55" stop-color="#9b8a7c"/>
          <stop offset="1" stop-color="#2b2a2e"/>
        </linearGradient>
      </defs>
      <polygon points="392,208 871,208 871,530 470,530" fill="url(#photoTone)"/>
    </svg>

    <section class="intro">
      <h1>PRIVATVERMIETER<br>SIND KEINE<br>MIETKONZERNE.</h1>
      <p>Steigende Kosten für Baustoffe und Handwerker bei Sanierung oder Renovierung machen in vielen Fällen eine Erhöhung der Miete leider erforderlich. Dabei geht es nicht um Gewinnmaximierung - privates Vermieten droht immer mehr zum Draufzahlgeschäft zu werden.</p>
    </section>

    <section class="state-box">
      <h2>Der Staat lässt private Vermieter im Regen stehen</h2>
      <p>Für Mietkonzerne ist es in der Regel kein Problem ausreichend Vergleichsmieten vorzuweisen, denn diese verfügen normalerweise selbst über ausreichend Immobilien die genutzt werden können.</p>
      <p>Private Vermieter jedoch, haben in Regionen ohne Mietspiegel nahezu keine Möglichkeit eine Mieterhöhung durchzusetzen - trotz steigender gesetzlicher Anforderungen an bestehendem Wohnraum.</p>
    </section>

    <section class="rent-why">
      <h2>Warum ist es wichtig, dass Vermieten rentabel ist?</h2>
      <p>Private Vermietung ist eine soziale Investition. Menschen investieren Ihr Geld in Wohnraum für andere. Das passiert allerdings nur, wenn man damit keine Verluste macht.</p>
      <p>Ist dies nicht mehr der Fall, erfolgt oft der Verkauf an Investoren. Das Problem dabei ist, dass diese oft nur an der Wertentwicklung der Immobilie interessiert sind. Häufig stehen diese Wohnungen leer oder werden luxussaniert für einen Weiterverkauf.</p>
      <p>Wohnraum wird damit verknappt und der Druck am Wohnungsmarkt erhöht sich. Eine Entwicklung die gesellschaftlich problematisch ist.</p>
      <p>Dies lässt sich nur verhindern, wenn Vermieter einen angemessenen Mietzins fordern bzw. erhalten. Dies liegt gleichermaßen im Interesse von Mietern und Vermietern. Nur so ist Vermietung auch nachhaltig.</p>
    </section>

    <section class="solution">
      <h2>Mieterhöhungen sind in Orten ohne Mietspiegel fast unmöglich. Die Lösung?</h2>
      <p>Ortsübliche Vergleichsmieten. Unsere Plattform bietet Zugang zu ortsüblichen Vergleichsmieten.</p>
    </section>

    <div class="web">www.mietwert.de</div>
  </main>
</body>
</html>
```